Employee Benefits Consulting Firm needs a refreshed website

I have a business (an employee benefits consulting firm) called Korvane Benefits Group, LLC (www.korvanebenefits-example.com).  The existing site is currently hosted on Plumhaven.  The business has been pretty much dormant since 2012.  I've relaunched the business and need a new website and looking for the website to be in Wordpress and to start with just 5 pages:
Home
About Us
Services
Contact Us
Blog
Some information about Korvane Benefits Group:
There is a tremendous waste (financial) in the traditional employee benefit model --- the current system is broken and simply stated, unsustainable. We take a very different approach when it comes to employee benefits consulting, constantly strive to provide short-term and long-term cost containment strategies that truly bend the healthcare cost curve... Many of our clients consider us as Benefit Architects...
Each employer/business is unique.
In short, our firm works with Employers to first understand their business.... -their history, their corporate structure, their leadership, their values, their uniqueness, etc.
Then we take a deep dive and get a strong grasp on their existing benefits program... -how did they get to where they are today, what are their goals/objectives, what is their risk tolerance, what are current pain points, are they compliant, etc.
Then after thorough analysis, we deliver a tailored solution. We implement the programs and manage the various aspects and moving parts of the program throughout the year.
We also are constantly analyzing the performance of the plan and monitor population health. We aggregate data and constantly refine the approach/strategy.

Updates
I made a few updates to the brief over the past couple of days...below is the updated brief:
Home
About Us
Services
Contact Us
Blog
MUST HAVE:
Mobile Friendly
PLEASE USE MERIDOX THEME
SHOULD HAVE:
the ability to add embedded video client testimonials
the ability for online chat
SHOULD NOT HAVE:
Photos from the old/existing website, I apologize for the late directive

I apologize for the delay on responding. Content is just about complete and will submit ASAP. Please let me know your availability to complete this project.

Updated content has been posted to this project.  I appreciate everybody's patience as we are working through this!

Target Market(s)
This is a BtoB website, primarily focusing on the following targets: CFOs, CEOs, Directors of Human Resources
Industry/Entity Type
Consulting
Number of Pages Required
5+ page
Requirements
Must have
- Mobile Friendly
- PLEASE USE MERIDOX THEME
Nice to have
- the ability to add embedded video client testimonials
- the ability for online chat
Should not have
- Photos from the old/existing website, I apologise for the late directive

```html
<!DOCTYPE html>
<html lang="en">
<head>
<meta charset="utf-8">
<title>Korvane Benefits Group</title>
<link href="https://fonts.googleapis.com/css2?family=Poppins:wght@400;500;600;700&family=Open+Sans:wght@400;600;700&display=swap" rel="stylesheet">
<style>
:root{
  --orange:#f26522;
  --orange-dark:#d9531a;
  --purple:#4b2f9b;
  --green:#6cbf4a;
  --ink:#1f1f1f;
  --text:#555;
  --muted:#8a8a8a;
  --light:#f4f4f4;
  --footer:#1b1b1b;
  --white:#fff;
}
*{box-sizing:border-box;margin:0;padding:0}
html,body{width:1200px;height:3310px;overflow:hidden}
body{font-family:"Open Sans",Arial,sans-serif;color:var(--text);background:var(--white);position:relative}
h1,h2,h3,h4,.heading{font-family:"Poppins",Arial,sans-serif;color:var(--ink)}
section,header,footer{position:absolute;left:0;width:1200px}

/* hero */
.hero{top:0;height:486px;overflow:hidden}
.hero-photo{position:absolute;inset:0;background:linear-gradient(100deg,#2a2d33 0%,#454a52 35%,#6b6f74 60%,#3b3f45 100%)}
.hero-shade{position:absolute;inset:0;background:linear-gradient(90deg,rgba(20,22,28,.75) 0%,rgba(20,22,28,.35) 55%,rgba(20,22,28,.1) 100%)}
.topbar{position:absolute;left:232px;top:7px;width:736px;height:68px;background:var(--white);display:flex;align-items:center;padding:0 22px}
.brand{display:flex;align-items:center;gap:8px;font-family:"Poppins",sans-serif;font-weight:600;font-size:15px;color:var(--purple)}
.brand-dot{width:14px;height:14px;border-radius:50%;background:var(--orange)}
.contact-bits{margin-left:auto;display:flex;gap:30px;font-size:9.5px;line-height:1.45;color:#444}
.contact-bits b{color:var(--ink)}
.contact-bits .item{display:flex;gap:6px}
.navbar{position:absolute;left:232px;top:75px;width:736px;height:35px;background:var(--purple);display:flex;padding-left:50px}
.navbar a{color:#fff;font-family:"Poppins",sans-serif;font-size:11px;font-weight:500;text-decoration:none;padding:0 14px;line-height:35px}
.navbar a.active{background:rgba(255,255,255,.12);border-bottom:3px solid var(--orange)}
.hero h1{position:absolute;left:232px;top:186px;color:#fff;font-size:36px;line-height:41px;font-weight:700;letter-spacing:-.5px}
.hero h1 em{font-style:normal;color:var(--orange)}
.hero-lead{position:absolute;left:232px;top:276px;width:380px;color:#e6e6e6;font-size:11.5px;line-height:17px}
.btn{display:inline-block;font-family:"Poppins",sans-serif;font-weight:600;font-size:9px;text-transform:uppercase;color:#fff;text-align:center;text-decoration:none}
.hero .btn{position:absolute;left:232px;top:330px;width:104px;height:26px;line-height:26px;background:var(--orange)}
.slide-arrow{position:absolute;width:22px;height:22px;border-radius:50%;display:flex;align-items:center;justify-content:center}
.hero .prev{left:112px;top:232px;background:rgba(255,255,255,.25)}
.hero .next{left:1066px;top:232px;background:var(--orange)}

/* services */
.services{top:486px;height:254px}
.eyebrow{font-family:"Poppins",sans-serif;font-size:8.5px;font-weight:600;letter-spacing:.5px;text-transform:uppercase;color:var(--orange)}
.services .intro{position:absolute;left:254px;top:34px;width:250px}
.services h2{font-size:21px;font-weight:700;margin-top:4px}
.services .intro p{font-size:10.5px;line-height:16px;margin-top:6px}
.text-link{font-size:10.5px;color:var(--green);text-decoration:underline;font-weight:600}
.services .intro .text-link{position:absolute;top:176px;left:0}
.service{position:absolute;top:30px;width:176px;text-align:center}
.service p{font-size:10.5px;line-height:15.5px;margin-top:8px}
.service h3{font-size:13px;font-weight:500;margin-top:6px}
.service .text-link{position:absolute;top:180px;left:0;right:0}

/* how we work */
.process{top:740px;height:390px;background:var(--orange);overflow:hidden}
.process-photo{position:absolute;left:0;top:0;width:640px;height:390px;background:linear-gradient(110deg,#a8461c 0%,#cf5a22 45%,#e8642a 80%,var(--orange) 100%)}
.process h2{position:absolute;left:628px;top:64px;color:#fff;font-size:21px;font-weight:700}
.process .sub{position:absolute;left:628px;top:96px;color:#fff;font-size:11px}
.step{position:absolute;display:flex;align-items:flex-end;gap:6px;color:#fff}
.step .num{font-family:"Poppins",sans-serif;font-weight:700;font-size:52px;line-height:48px}
.step .meta{display:flex;flex-direction:column;gap:4px}
.step .label{font-family:"Poppins",sans-serif;font-weight:600;font-size:11px}

/* team */
.team{top:1130px;height:477px}
.section-title{position:absolute;left:0;width:1200px;text-align:center;font-size:20px;font-weight:600}
.team .section-title{top:60px}
.member{position:absolute;top:114px;width:232px;text-align:center}
.member .photo{height:243px;width:232px}
.member h4{font-size:12.5px;font-weight:600;margin-top:20px}
.member .role{font-size:9px;color:var(--orange);margin-top:2px}
.team .prev{left:176px;top:225px;background:#e5e5e5}
.team .next{left:990px;top:225px;background:var(--orange)}

/* testimonials */
.testimonials{top:1607px;height:438px;background:var(--light)}
.testimonials .section-title{top:72px}
.quote-mark{position:absolute;left:584px;top:142px;font-family:"Poppins",sans-serif;font-size:60px;line-height:40px;color:#cfcfcf;font-weight:700}
.avatar{position:absolute;left:576px;top:201px;width:48px;height:48px;border-radius:50%;background:linear-gradient(135deg,#c9c9c9,#8e8e8e)}
.client{position:absolute;left:0;width:1200px;top:268px;text-align:center;font-size:10.5px;font-weight:700;color:var(--ink)}
.client span{color:var(--orange);font-weight:600}
.quote{position:absolute;left:330px;width:540px;top:298px;text-align:center;font-size:12px;line-height:21px;font-style:italic;color:#444}
.dots{position:absolute;left:586px;top:392px;display:flex;gap:5px}
.dots i{width:5px;height:5px;border-radius:50%;background:#bbb;display:block}
.dots i.on{background:var(--orange)}

/* newsletter */
.newsletter{top:2045px;height:128px;background:var(--purple)}
.newsletter h3{position:absolute;left:236px;top:44px;color:#fff;font-size:17px;font-weight:600}
.newsletter p{position:absolute;left:236px;top:68px;color:#ddd;font-size:9.5px}
.newsletter .field{position:absolute;left:592px;top:54px;width:254px;height:30px;background:#fff;font-size:9.5px;color:#999;padding:0 12px;line-height:30px}
.newsletter .btn{position:absolute;left:846px;top:54px;width:117px;height:30px;line-height:30px;background:var(--green)}

/* blog */
.blog{top:2173px;height:490px}
.blog .eyebrow{position:absolute;left:0;width:1200px;text-align:center;top:74px}
.blog .section-title{top:88px}
.post{position:absolute;top:130px;width:232px;text-align:center}
.post .thumb{height:152px}
.post h4{font-size:12px;font-weight:600;margin-top:18px}
.post .date{font-size:8.5px;color:var(--muted);margin-top:4px}
.post p{font-size:9.5px;line-height:15px;margin-top:8px}
.post .btn{width:104px;height:27px;line-height:27px;background:var(--green);margin-top:12px;font-size:8px}

/* contact */
.contact{top:2663px;height:347px;background:var(--orange);overflow:hidden}
.contact-photo{position:absolute;inset:0;background:linear-gradient(90deg,var(--orange-dark) 0%,var(--orange) 50%,#e4622a 100%)}
.contact h2{position:absolute;left:0;width:1200px;text-align:center;top:56px;color:#fff;font-size:21px;font-weight:700}
.input{position:absolute;background:#fff;font-size:9.5px;color:#555;padding:0 10px;line-height:32px;height:32px}
.contact .btn{position:absolute;left:495px;top:258px;width:217px;height:31px;line-height:31px;background:var(--green)}

/* footer */
.footer{top:3010px;height:300px;background:var(--footer);color:#bbb}
.footer .brand{position:absolute;left:236px;top:40px;color:#fff;font-size:15px}
.footer .about{position:absolute;left:236px;top:106px;width:180px;font-size:9.5px;line-height:16px}
.footer h5{position:absolute;font-family:"Poppins",sans-serif;font-size:9.5px;color:#fff;font-weight:600;text-transform:uppercase;border-bottom:2px solid var(--orange);padding-bottom:2px}
.fcol{position:absolute;font-size:9.5px;line-height:15px}
.fcol .lbl{color:var(--orange);font-weight:700;font-size:8px;text-transform:uppercase;margin-top:8px}
.fmenu{position:absolute;list-style:none;font-size:10px;line-height:26px}
.social{position:absolute;left:919px;top:80px;display:flex;gap:9px}
.social i{display:block;width:8px;height:8px;border-radius:50%;background:#ddd}
.copyright{position:absolute;left:0;width:1200px;top:270px;text-align:center;font-size:8.5px;color:#777;border-top:1px solid #2c2c2c;padding-top:10px}
</style>
</head>
<body>

<header class="hero">
  <div class="hero-photo" role="img" aria-label="Photo of smiling colleagues in a bright office"></div>
  <div class="hero-shade"></div>
  <div class="topbar">
    <div class="brand"><span class="brand-dot"></span>Korvane Benefits Group</div>
    <div class="contact-bits">
      <div class="item">
        <svg width="10" height="10" viewBox="0 0 24 24"><path fill="#6cbf4a" d="M6.6 10.8a15 15 0 0 0 6.6 6.6l2.2-2.2c.3-.3.7-.4 1-.2 1.1.4 2.3.6 3.6.6.6 0 1 .4 1 1V20c0 .6-.4 1-1 1A17 17 0 0 1 3 4c0-.6.4-1 1-1h3.5c.6 0 1 .4 1 1 0 1.3.2 2.5.6 3.6.1.3 0 .7-.2 1z"/></svg>
        <div>Main Number: <b>(555) 014-2280</b><br>Toll-Free: <b>(555) 019-7741</b></div>
      </div>
      <div class="item">
        <svg width="10" height="12" viewBox="0 0 24 24"><path fill="#6cbf4a" d="M12 2a7 7 0 0 0-7 7c0 5.2 7 13 7 13s7-7.8 7-13a7 7 0 0 0-7-7zm0 9.5A2.5 2.5 0 1 1 12 6.5a2.5 2.5 0 0 1 0 5z"/></svg>
        <div><b>Dallas Office Location</b><br>4120 Northgate Parkway, Suite 300<br>Dallas, Texas 75200</div>
      </div>
    </div>
  </div>
  <nav class="navbar">
    <a class="active" href="#">Home</a><a href="#">About Us</a><a href="#">Services</a><a href="#">Contact Us</a><a href="#">Blog</a>
  </nav>
  <h1>The <em>key</em> to benefits<br>is to be <em>competitive</em></h1>
  <p class="hero-lead">At Korvane Benefits Group we know your company gains competitive advantages from an experienced and hard working team.</p>
  <a class="btn" href="#">Contact Us</a>
  <span class="slide-arrow prev"><svg width="8" height="8" viewBox="0 0 10 10"><path d="M7 1 3 5l4 4" stroke="#fff" stroke-width="2" fill="none"/></svg></span>
  <span class="slide-arrow next"><svg width="8" height="8" viewBox="0 0 10 10"><path d="M3 1l4 4-4 4" stroke="#fff" stroke-width="2" fill="none"/></svg></span>
</header>

<section class="services">
  <div class="intro">
    <div class="eyebrow">Our Services</div>
    <h2>What We Do For You</h2>
    <p>Saving money on employee benefits while still attracting and retaining the best and the brightest is a must in today's economy. The cost of providing benefits is rising significantly, while employees consistently seek more and more from their benefits packages.</p>
    <a class="text-link" href="#">More Services</a>
  </div>
  <div class="service" style="left:534px">
    <svg width="64" height="62" viewBox="0 0 64 62" fill="none" stroke="#222" stroke-width="2">
      <path d="M14 22h12a5 5 0 1 1 10 0h12v12a5 5 0 1 0 0 10v12H14V44a5 5 0 1 1 0-10z" stroke="#f26522"/>
      <path d="M4 30l10-10M60 30 50 20"/>
    </svg>
    <p>Your employees are your most valuable assets. Helping them stay healthy and productive not only benefits workers and their families.</p>
    <a class="text-link" href="#">Read More</a>
  </div>
  <div class="service" style="left:778px">
    <svg width="64" height="62" viewBox="0 0 64 62" fill="none" stroke="#222" stroke-width="2">
      <circle cx="32" cy="18" r="11" stroke="#f26522"/>
      <path d="M28 30v6h8v-6"/>
      <circle cx="14" cy="40" r="5"/><circle cx="50" cy="40" r="5"/>
      <path d="M6 58c0-7 4-11 8-11s8 4 8 11M42 58c0-7 4-11 8-11s8 4 8 11"/>
    </svg>
    <h3>Korvane Assurance</h3>
    <p style="margin-top:4px">Whether you want to make sure the mortgage will get paid, your children will go to college</p>
    <a class="text-link" href="#">Read More</a>
  </div>
</section>

<section class="process">
  <div class="process-photo" role="img" aria-label="Photo of a team reviewing work together, tinted orange"></div>
  <h2>How We Work</h2>
  <p class="sub">More Control. More Care. More Savings.</p>
  <div class="step" style="left:632px;top:155px">
    <span class="num">1</span>
    <div class="meta">
      <svg width="30" height="30" viewBox="0 0 30 30" fill="none" stroke="#fff" stroke-width="2"><rect x="5" y="4" width="20" height="24" rx="2"/><path d="M10 12l2 2 4-4M10 20h10"/></svg>
      <span class="label">Plan &amp; Analyze</span>
    </div>
  </div>
  <div class="step" style="left:831px;top:155px">
    <span class="num">2</span>
    <div class="meta">
      <svg width="30" height="30" viewBox="0 0 30 30" fill="none" stroke="#fff" stroke-width="2"><rect x="3" y="5" width="18" height="18"/><path d="M7 11h10M7 16h6"/><path d="M21 13l6 6-6 6"/></svg>
      <span class="label">Design &amp; Build</span>
    </div>
  </div>
  <div class="step" style="left:632px;top:265px">
    <span class="num">3</span>
    <div class="meta">
      <svg width="30" height="30" viewBox="0 0 30 30" fill="none" stroke="#fff" stroke-width="2"><circle cx="15" cy="15" r="6"/><path d="M15 3v4M15 23v4M3 15h4M23 15h4M6.5 6.5l3 3M20.5 20.5l3 3M6.5 23.5l3-3M20.5 9.5l3-3"/></svg>
      <span class="label">Implement</span>
    </div>
  </div>
  <div class="step" style="left:831px;top:265px">
    <span class="num">4</span>
    <div class="meta">
      <svg width="30" height="30" viewBox="0 0 30 30" fill="none" stroke="#fff" stroke-width="2"><path d="M3 25l7-8 5 5 12-14"/><path d="M21 8h6v6"/></svg>
      <span class="label">Manage Year Round</span>
    </div>
  </div>
</section>

<section class="team">
  <h2 class="section-title">Meet Our Teams</h2>
  <span class="slide-arrow prev"><svg width="8" height="8" viewBox="0 0 10 10"><path d="M7 1 3 5l4 4" stroke="#999" stroke-width="2" fill="none"/></svg></span>
  <div class="member" style="left:234px">
    <div class="photo" role="img" aria-label="Portrait of the company president" style="background:linear-gradient(180deg,#d9dcdf,#9aa0a6)"></div>
    <h4>Martin Ellery CBC</h4><div class="role">President</div>
  </div>
  <div class="member" style="left:484px">
    <div class="photo" role="img" aria-label="Portrait of an employee benefit consultant" style="background:linear-gradient(180deg,#b9cfe0,#6e8fa8)"></div>
    <h4>Owen Castrell CBC</h4><div class="role">Employee Benefit Consultant</div>
  </div>
  <div class="member" style="left:736px">
    <div class="photo" role="img" aria-label="Portrait of an employee benefits consultant" style="background:linear-gradient(180deg,#c7c2ba,#8a7d6e)"></div>
    <h4>Helena Brooke</h4><div class="role">Employee Benefits Consultant</div>
  </div>
  <span class="slide-arrow next"><svg width="8" height="8" viewBox="0 0 10 10"><path d="M3 1l4 4-4 4" stroke="#fff" stroke-width="2" fill="none"/></svg></span>
</section>

<section class="testimonials">
  <h2 class="section-title">Client testimonials</h2>
  <div class="quote-mark">&ldquo;</div>
  <div class="avatar" role="img" aria-label="Client portrait"></div>
  <div class="client">Nora Whitfield - <span>HR Manager / City of Ashbury</span></div>
  <p class="quote">" Korvane was able to save the City enough money on our current insurance that we were able to provide our employees with an additional benefit of Long Term Disability."</p>
  <div class="dots"><i></i><i></i><i class="on"></i></div>
</section>

<section class="newsletter">
  <h3>Email Newsletters</h3>
  <p>Keep me up to date with content, updates, and offers from Korvane.</p>
  <div class="field">Email address</div>
  <a class="btn" href="#">Subscribe</a>
</section>

<section class="blog">
  <div class="eyebrow">Latest News</div>
  <h2 class="section-title">From Blog News</h2>
  <article class="post" style="left:234px">
    <div class="thumb" role="img" aria-label="Photo of colleagues meeting around a laptop" style="background:linear-gradient(135deg,#6d7278,#c3c6c9)"></div>
    <h4>velit aliquetpraesent commodo</h4>
    <div class="date">February 3, 2019</div>
    <p>Integer posuere erat a ante venenatis dapibus posuere velit aliquetpraesent commodo cursus magna.</p>
    <a class="btn" href="#">Read More</a>
  </article>
  <article class="post" style="left:484px">
    <div class="thumb" role="img" aria-label="Photo of a team working under warm cafe lights" style="background:linear-gradient(135deg,#5a3a26,#b9835a)"></div>
    <h4>velit aliquetpraesent commodo</h4>
    <div class="date">February 3, 2019</div>
    <p>Integer posuere erat a ante venenatis dapibus posuere velit aliquetpraesent commodo cursus magna.</p>
    <a class="btn" href="#">Read More</a>
  </article>
  <article class="post" style="left:734px">
    <div class="thumb" role="img" aria-label="Photo of a smiling business team standing together" style="background:linear-gradient(135deg,#8a8f95,#d6d8da)"></div>
    <h4>velit aliquetpraesent commod</h4>
    <div class="date">February 3, 2019</div>
    <p>Integer posuere erat a ante venenatis dapibus posuere velit aliquetpraesent commodo cursus magna.</p>
    <a class="btn" href="#">Read More</a>
  </article>
</section>

<section class="contact">
  <div class="contact-photo" role="img" aria-label="Photo of people in an office, tinted orange"></div>
  <h2>Contact Us</h2>
  <div class="input" style="left:236px;top:99px;width:239px">Name</div>
  <div class="input" style="left:493px;top:99px;width:230px">Email</div>
  <div class="input" style="left:740px;top:99px;width:232px">Subject</div>
  <div class="input" style="left:236px;top:144px;width:736px;height:90px">Message</div>
  <a class="btn" href="#">Submit Now</a>
</section>

<footer class="footer">
  <div class="brand"><span class="brand-dot"></span>Korvane Benefits Group</div>
  <p class="about">Our innovative team approach blends your unique needs with our creative thinking, comprehensive expertise, and in-depth resources to help you and your employees with benefit management, plan design, and employee communication.</p>
  <h5 style="left:477px;top:46px">Contact Us</h5>
  <div class="fcol" style="left:477px;top:64px">
    <div class="lbl">Business Address</div>
    Dallas Office Location<br>4120 Northgate Parkway, Suite 300<br>Dallas, Texas 75200
    <div class="lbl">Business Phone</div>
    Main Number: (555) 014-2280<br>Toll-Free: (555) 019-7741
    <div class="lbl">Business Email</div>
    info@korvanebenefits-example.com
  </div>
  <h5 style="left:692px;top:46px">Menu</h5>
  <ul class="fmenu" style="left:692px;top:70px"><li>Home</li><li>About Us</li><li>Services</li><li>Contact Us</li><li>Blog</li></ul>
  <ul class="fmenu" style="left:778px;top:70px"><li>Terms of Use</li><li>Privacy Policy</li></ul>
  <div class="social"><i></i><i></i><i></i></div>
  <div class="copyright">Copyright 2019 All Rights Reserved. Korvane Benefits Group, LLC</div>
</footer>

</body>
</html>
```